RQW Structural Approval Standards Private Assessors

Professional Construction Consultancy Company Business Card - must keep logo colours see images below - examples have been added from my last competition - please see them as examples only!

Target Market(s)

Home Builders

Industry/Entity Type

Construction

Contact Information for Business Card

See "must haves"

Font styles to use
Sans Serif

Colors
ffffff
add136
000000

Requirements
Must have
• Daniel Moravi
• Director
• Phone: 0431 587 219
• Address: 7 Tarrunga Rd,
• Hallworth Vale, SA, 5091
• Email: rqwassessors@mailbox-example.com
• Website: www.rqwassessors-example.com.au
• Facebook: RQW Structural Approval Standards
Nice to have
• Side 1: full logo
• Side 2: company details
Should not have
• hard to read
• must be clear and professional

```html
<!DOCTYPE html>
<html lang="en">
<head>
<meta charset="utf-8">
<title>RQW Structural Approval Standards – Business Card</title>
<link rel="stylesheet" href="https://fonts.googleapis.com/css2?family=Lato:ital,wght@0,400;1,400&family=Montserrat:wght@500;700&display=swap">
<style>
  :root {
    --stage: #262626;
    --card: #ffffff;
    --brand-green: #add136;
    --ink: #000000;
    --body-text: #333333;
    --social: #3b5998;
  }
  * { margin: 0; padding: 0; box-sizing: border-box; }
  html, body {
    width: 1200px; height: 1000px; overflow: hidden;
    background: var(--stage);
  }
  .card {
    position: absolute; left: 358px; width: 484px; height: 277px;
    background: var(--card);
  }
  .card--front { top: 162px; }
  .card--back { top: 527px; }

  .wordmark {
    position: absolute; display: flex; align-items: center; gap: 10px;
    font-family: "Montserrat", sans-serif; font-weight: 700;
    color: var(--ink); text-transform: uppercase; line-height: 1.15;
  }
  .wordmark__square { flex: none; background: var(--brand-green); }
  .card--front .wordmark {
    left: 112px; top: 72px; width: 262px; height: 80px;
    font-size: 15px; letter-spacing: 0.5px;
  }
  .card--front .wordmark__square { width: 62px; height: 62px; }
  .card--back .wordmark {
    right: 28px; top: 30px; width: 196px; height: 60px;
    font-size: 11.5px; letter-spacing: 0.4px;
    flex-direction: row-reverse; text-align: right;
  }
  .card--back .wordmark__square { width: 46px; height: 46px; }

  .tagline {
    position: absolute; left: 80px; top: 174px; width: 332px;
    font-family: "Lato", sans-serif; font-style: italic; font-weight: 400;
    font-size: 13px; line-height: 16px; color: var(--body-text);
    text-align: justify; text-align-last: center;
  }
  .social-square {
    position: absolute; left: 432px; top: 227px; width: 27px; height: 27px;
    background: var(--social);
  }

  .person { position: absolute; left: 28px; top: 100px; font-family: "Montserrat", sans-serif; }
  .person__name { font-size: 21px; font-weight: 500; color: var(--ink); line-height: 26px; }
  .person__surname { color: var(--brand-green); }
  .person__role { font-size: 17px; font-weight: 500; color: var(--ink); line-height: 22px; }

  .contact {
    position: absolute; left: 28px; top: 157px;
    font-family: "Lato", sans-serif; font-size: 14.5px; line-height: 18.5px;
    letter-spacing: 0.3px; color: var(--body-text); list-style: none;
  }
  .contact__address { margin-top: 6px; }
</style>
</head>
<body>
  <section class="card card--front" aria-label="Business card front">
    <div class="wordmark">
      <span class="wordmark__square"></span>
      <span class="wordmark__name">RQW Structural Approval Standards Private Assessors</span>
    </div>
    <p class="tagline">Professionals in Privately Certified Residential and Commercial Structural Approval Standards for Council Development Approvals</p>
    <span class="social-square" role="img" aria-label="Social profile: RQW Structural Approval Standards"></span>
  </section>

  <section class="card card--back" aria-label="Business card back">
    <div class="wordmark">
      <span class="wordmark__square"></span>
      <span class="wordmark__name">RQW Structural Approval Standards Private Assessors</span>
    </div>
    <div class="person">
      <p class="person__name">Daniel <span class="person__surname">Moravi</span></p>
      <p class="person__role">Director</p>
    </div>
    <ul class="contact">
      <li>0431 587 219</li>
      <li>www.rqwassessors-example.com.au</li>
      <li>rqwassessors@mailbox-example.com</li>
      <li class="contact__address">7 Tarrunga Rd,</li>
      <li>Hallworth Vale, SA, 5091</li>
    </ul>
  </section>
</body>
</html>
```